quillnest.com redesign with wireframes, white space and custom form are very important

Need a new two column design that will convert easily to mobile responsive. Lots of white space. Winning design will probably be based on header area and making the custom form stand out. I want the header to be very much like www.tamvorlo.com except the form not to go up into the header.
Here are some of the websites I really like:
www.brisketdoors.com
http://plinkaroofsdirect.com/
http://dorvikamplandings.com/

We buy homes for cash and close fast. Our target is a home seller who is desperate to sell quickly.
I have uploaded my really ugly wireframe and my logo. I also uploaded my photo for the about us box and a possible photo to use for the header.
The copy on the wireframe is what I will be using except for the about us box.

Here is the exact link for video to frame in the top left box.
https://vidnook.example/Qp39xatLbRr

Number of Pages Required

1 page

Font styles to use
Sans Serif

Colors
0592cd
85cae6
eaf1f7
fbee3d
ec1f27

Requirements
Must have
• Everything on wireframe.
• Must use Verdana font and nothing should be smaller than 12 point. Most should be in 14 point. (except maybe inside of form)

```html
<!DOCTYPE html>
<html lang="en">
<head>
<meta charset="utf-8">
<title>quillnest.com – Sell Your Home Fast</title>
<link rel="stylesheet" href="https://fonts.googleapis.com/css2?family=Open+Sans:ital,wght@0,400;0,600;0,700;1,400&family=Raleway:wght@400;500;600&display=swap">
<style>
:root{
  --blue:#0592cd;
  --blue-deep:#0a6eb0;
  --blue-light:#85cae6;
  --pale:#eaf1f7;
  --yellow:#fbee3d;
  --red:#ec1f27;
  --red-deep:#c8101a;
  --ink:#222;
  --muted:#555;
  --line:#d4d4d4;
}
*{margin:0;padding:0;box-sizing:border-box}
html,body{width:673px;height:1200px;overflow:hidden;background:#fff}
body{position:relative;font-family:"Open Sans",Verdana,sans-serif;color:var(--ink)}
.abs{position:absolute}
.header-band{left:0;top:0;width:673px;height:152px;background:linear-gradient(#fff,#ececec);border-bottom:1px solid #ddd}
.brand{left:113px;top:22px;display:flex;align-items:center;gap:5px;font-family:"Open Sans",sans-serif;font-weight:700;font-size:12px;color:var(--red)}
.brand-mark{width:10px;height:10px;background:var(--red)}
.call{left:477px;top:8px;font-size:8.5px;color:#333;line-height:1.1}
.call small{display:block;font-size:6.2px}
.call strong{display:block;color:var(--red);font-weight:400;font-size:10px;margin-top:4px}
.nav{top:46px;font-size:7.2px;color:#333;letter-spacing:.2px}
.hero{left:113px;top:70px;width:447px;height:199px;background:linear-gradient(#3a7cc8 0%,#6aa1d6 35%,#6f7d5a 60%,#3d5a2a 85%,#4f6b33 100%)}
.hero-title{left:113px;width:447px;text-align:center;color:#fff;font-family:"Raleway",sans-serif;font-weight:600;font-size:13.5px;text-transform:uppercase;text-shadow:0 1px 2px rgba(0,0,0,.5)}
.dots{left:318px;top:255px;display:flex;gap:3px}
.dots i{width:6px;height:6px;border-radius:50%;background:#fff}
.h-sec{font-family:Verdana,"Open Sans",sans-serif;font-size:9.5px;color:#111}
.benefits{left:114px;top:309px;font-size:5.6px;color:#444;list-style:none}
.benefits li{display:flex;align-items:center;gap:5px;height:11.5px}
.benefits svg{width:7px;height:7px}
.video{left:113px;top:373px;width:195px;height:117px;background:linear-gradient(#1d2b45,#4a4030 60%,#2a2a20);border:1px solid #333}
.play{left:198px;top:420px;width:22px;height:22px;border-radius:50%;background:#fff}
.body-copy{font-size:5.3px;line-height:11px;color:#444}
.reasons{left:118px;top:622px;list-style:none;font-size:5.8px;color:#333}
.reasons li{height:11.5px}
.feature-img{width:85px;height:50px}
.feature h3{font-family:"Open Sans",sans-serif;font-weight:600;font-size:7.3px;color:var(--red)}
.feature p{font-size:5.2px;line-height:8.2px;color:#555;width:150px;margin-top:2px}
.side-menu{left:116px;top:926px;width:242px;list-style:none}
.side-menu li{height:16.3px;border:1px solid #cfcfcf;border-bottom:none;background:linear-gradient(#fbfbfb,#e7e7e7);font-size:6px;color:#222;padding:4px 13px}
.side-menu li:last-child{border-bottom:1px solid #cfcfcf}
.lead-form{left:370px;top:288px;width:190px;height:202px;background:linear-gradient(var(--blue),var(--blue-deep));padding:14px 13px 0 16px;color:#fff}
.lead-form h2{font-family:"Raleway",sans-serif;font-weight:500;font-size:10.2px}
.lead-form p{font-size:6px;margin:3px 0 8px}
.field{height:14px;background:linear-gradient(#fff,#e9e9e9);margin-bottom:4px;font-size:5px;color:#666;padding:3px 6px;width:161px}
.submit{width:161px;height:19px;background:var(--red);color:#fff;margin-top:5px;font-size:5.2px;display:flex;align-items:center;justify-content:center;gap:3px}
.submit b{font-size:8px;font-weight:600}
.share-bar{left:368px;top:498px;width:192px;height:22px;border:1px solid #cfcfcf;background:linear-gradient(#fafafa,#e6e6e6);display:flex}
.share-bar div{flex:1;display:flex;align-items:center;font-size:6.4px}
.share-bar div+div{border-left:1px solid #cfcfcf;justify-content:center;gap:4px}
.share-bar i{width:7px;height:7px;border-radius:50%;background:var(--blue)}
.note{left:368px;top:526px;font-size:6.2px;color:#666}
.side-panel{left:368px;top:547px;width:192px;height:373px;border:1px solid #cfcfcf}
.panel-title{font-family:"Raleway",sans-serif;font-size:9.3px;color:#222}
.divider{height:1px;background:#cfcfcf;width:192px;left:368px}
.about-photo{left:378px;top:659px;width:52px;height:49px;background:linear-gradient(#8aa0b8,#c79a80 55%,#3a4a60)}
.small{font-size:5.2px;line-height:9.8px;color:#555}
.promo-img{left:368px;top:926px;width:192px;height:80px;background:linear-gradient(#1a2a4a,#3b4d6a 50%,#7a6640)}
.promo-cap{left:368px;top:1006px;width:192px;height:18.5px;background:var(--yellow);font-size:6.4px;text-align:center;line-height:18.5px;color:#222}
.footer{left:0;top:1050px;width:673px;height:123px;background:linear-gradient(var(--red),#d81a22)}
.footer-col h4{font-family:"Raleway",sans-serif;font-weight:500;font-size:11px;color:#fff;margin-bottom:6px}
.footer-col li{list-style:none;font-size:6.4px;color:#fff;height:12px}
.footer-rule{width:1px;height:78px;top:1074px;background:rgba(255,255,255,.55)}
.legal{left:0;top:1173px;width:673px;height:27px;background:var(--red-deep);font-size:5.3px;color:#fff;padding:11px 0 0 118px}
</style>
</head>
<body>
<div class="abs header-band"></div>
<div class="abs brand"><span class="brand-mark"></span>quillnest.com</div>
<div class="abs call">CALL US<small>Nights and weekends ok</small><strong>555-203-1847</strong></div>
<span class="abs nav" style="left:210px">SELL YOUR HOME</span>
<span class="abs nav" style="left:294px">HOW IT WORKS</span>
<span class="abs nav" style="left:370px">STOP FORECLOSURE</span>
<span class="abs nav" style="left:464px">PROBATE</span>
<span class="abs nav" style="left:515px">CONTACT</span>

<div class="abs hero" role="img" aria-label="Photo of a single-storey white brick house with hedges under a blue sky"></div>
<div class="abs hero-title" style="top:142px">Sell your home for cash in 8 days</div>
<div class="abs hero-title" style="top:160px">We buy houses nationwide</div>
<div class="abs dots"><i></i><i></i><i></i><i></i></div>

<h2 class="abs h-sec" style="left:112px;top:288px">These are the benefits of selling your home to us</h2>
<ul class="abs benefits">
  <li><svg viewBox="0 0 10 10"><circle cx="5" cy="5" r="5" fill="#ec1f27"/><path d="M2.6 5.2l1.7 1.7 3.2-3.4" stroke="#fff" stroke-width="1.3" fill="none"/></svg>You pick the closing date</li>
  <li><svg viewBox="0 0 10 10"><circle cx="5" cy="5" r="5" fill="#ec1f27"/><path d="M2.6 5.2l1.7 1.7 3.2-3.4" stroke="#fff" stroke-width="1.3" fill="none"/></svg>You pay NO commissions or fees</li>
  <li><svg viewBox="0 0 10 10"><circle cx="5" cy="5" r="5" fill="#ec1f27"/><path d="M2.6 5.2l1.7 1.7 3.2-3.4" stroke="#fff" stroke-width="1.3" fill="none"/></svg>You don't have to paint, clean or make repairsa</li>
</ul>
<p class="abs h-sec" style="left:112px;top:353px;font-size:7.4px">Watch to see our president Darren explain how easy it is to sell to us</p>
<div class="abs video" role="img" aria-label="Video still of a modern house lit at dusk"></div>
<svg class="abs" style="left:198px;top:420px" width="22" height="22" viewBox="0 0 22 22"><circle cx="11" cy="11" r="11" fill="#fff"/><path d="M8.5 6.5v9l7-4.5z" fill="#111"/></svg>

<h2 class="abs h-sec" style="left:112px;top:501px;width:250px;line-height:11.5px">Sell your home or house fast for cash to a professional investor company.</h2>
<p class="abs h-sec" style="left:112px;top:527px;font-size:7.4px">We buy Houses and close quickly</p>
<p class="abs body-copy" style="left:112px;top:543px;width:236px">Selling a home on your own has never been easier. From Orlando to Greensboro - and all points in between- you can sell your home today without any hassles. Call 1-800-555-0142 or fill out the form below to get a written offer on your home in just 36 hours. Sell today online to people that carea</p>

<h2 class="abs h-sec" style="left:112px;top:602px;font-size:8.5px">If you need to sell a home fast because of:</h2>
<ul class="abs reasons">
  <li>Divorce or Bankruptcy</li>
  <li>Foreclosure</li>
  <li>Landlord problems - evictions with tenants okay</li>
  <li>Inherited property in probate</li>
  <li>Termites, mold, flood or fire damage, leaky roof</li>
  <li>Moving or can't afford mortgage payments</li>
</ul>
<h2 class="abs h-sec" style="left:114px;top:700px;font-size:8.5px">We Can Help. We are the fastest home buyers around.</h2>

<div class="abs feature-img" style="left:114px;top:734px;background:linear-gradient(#5a8ad0,#a05a3a 55%,#5a7a3a)" role="img" aria-label="Photo of a red brick family house"></div>
<div class="abs feature" style="left:207px;top:736px"><h3>Massa libero interdum nec</h3><p>interdum vel blandit sed nulla in ullamcorper est eget tempor cursus neque mi consectetuer mi a ultricies massa est sed nisl Class aptent taciti sociosqu ad litora torquent per conubia nostra per inceptos</p></div>
<div class="abs feature-img" style="left:114px;top:799px;background:linear-gradient(#1d2a5a,#4a5a8a 50%,#2a3040)" role="img" aria-label="Photo of a modern house at night"></div>
<div class="abs feature" style="left:207px;top:801px"><h3>Massa libero interdum nec</h3><p>interdum vel blandit sed nulla in ullamcorper est eget tempor cursus neque mi consectetuer mi a ultricies massa est sed nisl Class aptent taciti sociosqu ad litora torquent per conubia nostra per inceptos</p></div>
<div class="abs feature-img" style="left:115px;top:867px;background:linear-gradient(#3a4a7a,#8a8aa0 50%,#5a4a40)" role="img" aria-label="Photo of a contemporary villa at dusk"></div>
<div class="abs feature" style="left:208px;top:868px"><h3>Massa libero interdum nec</h3><p>interdum vel blandit sed nulla in ullamcorper est eget tempor cursus neque mi consectetuer mi a ultricies massa est sed nisl Class aptent taciti sociosqu ad litora torquent per conubia nostra per inceptos</p></div>

<ul class="abs side-menu">
  <li>Archives</li><li>Sell my house</li><li>Fast cash for homes</li><li>We buy houses</li><li>Real Estate investor</li><li>Latest</li>
</ul>

<form class="abs lead-form">
  <h2>Yes, I want to sell my home fast!</h2>
  <p>Get a no obligation written offer in 36 hours</p>
  <div class="field">Your Name</div>
  <div class="field">Your phone number</div>
  <div class="field">Your Email Address</div>
  <div class="field">Property Address including City, State and Zip Code</div>
  <div class="field">Repairs needed if any</div>
  <div class="field">Asking Price</div>
  <div class="field">Comments</div>
  <div class="submit"><b>Submit,</b> to get started selling your home fast.</div>
</form>

<div class="abs share-bar"><div style="padding-left:12px">Our Privacy Policy</div><div><i></i><i></i><i></i></div></div>
<p class="abs note">Call us 8am to 10 pm Eastern time. We answer our phones</p>

<div class="abs side-panel"></div>
<h3 class="abs panel-title" style="left:381px;top:559px">Home Seller Testimonials</h3>
<p class="abs small" style="left:376px;top:578px;width:175px;font-style:italic;line-height:10.5px"><span style="font-size:9px;color:#999">“</span> I just wanted to thank you for buying my home in Winter Park. You made it fast and easy and kept me well informed the whole way</p>
<p class="abs" style="left:381px;top:604px;font-size:6.2px;color:var(--red)">Lorna Pettifer – Winter Park</p>
<p class="abs" style="left:498px;top:622px;font-size:6.2px;color:#333">More Testimonials</p>
<div class="abs divider" style="top:634px"></div>
<h3 class="abs panel-title" style="left:379px;top:643px;color:var(--red)">About Us</h3>
<div class="abs about-photo" role="img" aria-label="Portrait photo of the company owner"></div>
<p class="abs small" style="left:438px;top:657px;width:112px;line-height:9.5px">Owned and operated in Orlando Florida since 2001. Oldest Continuous operated website in country</p>
<p class="abs small" style="left:438px;top:688px;width:112px;line-height:9.5px">In massa libero interdum nec interdum vel blandit sed nulla in ullamcorper</p>
<div class="abs divider" style="top:726px"></div>
<h3 class="abs panel-title" style="left:381px;top:742px;width:175px;font-size:8.5px;line-height:11.5px">Some of the cities where we buy houses. Not all are listed</h3>
<p class="abs small" style="left:381px;top:770px;width:172px">These are the cities where we have an affiliate where you can sell a home fast or quickly and we buy homes: Orlando Jacksonville Ft Myers Tampa St Pete Gainesville Tallahassee Melbourne West Palm Beach Apopka Deland Kissimmee Lakeland Ocala Chicago Philadelphia Camden Atlanta Valdosta Houston Detroit Phoenix Seattle Tacoma Portland Charlotte Cincinnati San Antonio Harrisburg Virginia Beach Virginia Homes Greensboro Charleston SC Flint Rochester Lake Florida Wilmington Columbia Titusville If you don't see your city, we still probably buy homes there</p>
<p class="abs small" style="left:381px;top:865px;width:172px">These are the types of real estate that we buy: We buy nice houses and outdated problem homes. We buy in great neighborhoods and not so nice. We buy block homes and frame homes. We buy</p>

<div class="abs promo-img" role="img" aria-label="Photo of a modern home lit up at night"></div>
<div class="abs promo-cap">We buy nice pretty houses and some ugly ones as well</div>

<footer>
  <div class="abs footer"></div>
  <div class="abs footer-col" style="left:122px;top:1071px"><h4>Company</h4><ul><li>Sell Your Home</li><li>How it Works</li><li>Stop Foreclosure</li><li>Probate</li><li>Contact</li></ul></div>
  <div class="abs footer-rule" style="left:202px"></div>
  <div class="abs footer-col" style="left:230px;top:1071px"><h4>Services</h4><ul><li>Mlibero interdum</li><li>Nec interdum</li><li>Ael blandit</li><li>Sed nulla</li><li>Aullamcorper est</li></ul></div>
  <div class="abs footer-rule" style="left:310px"></div>
  <div class="abs footer-col" style="left:345px;top:1071px"><h4>Resources</h4><ul><li>Testimonials</li><li>News</li><li>Security Alerts</li><li>Contact Us</li><li>Sitemap</li></ul></div>
  <div class="abs footer-rule" style="left:420px"></div>
  <div class="abs footer-col" style="left:453px;top:1071px"><h4>Contact Info</h4><ul><li>48 Calder Lane #4B Texas</li><li>75010 TX</li><li>555.212.0468</li><li>hello@quillnest.com</li></ul></div>
  <div class="abs legal">© 2015 Company Name &nbsp;All right reserved &nbsp;Term of Use</div>
</footer>
</body>
</html>
```